Lanternfield Systems Bi Fold Brocher

I need a bi fold (front/back page 1 & front/back page 2) color brochure designed to pass out to clients at a convention. My website is lanternfieldsys.example. Please take images and text from the website to create the brochure. Use the products and product descriptions to display what we offer. Use the text and quotes to describe what we do. Make it professional, descriptive, and full of useful information.

Industry/Entity Type

Business Software

Font styles to use
Serif

Colors
00a990
33b8a4
86cfc6
fbf289
0255a3
3377b5
85acd3

Requirements
Must have
• Contact Info:
• Address:
• 728 Mossgate Boulevard
• Building 200, Suite 1187
• Cumming, GA 30987
• Telephone: 1 (555) 274.8816
• Toll Free: 1 (800) 555.0147
• Email: contact@lanternfieldsys.example
Nice to have
• Good backrounds

```html
<!DOCTYPE html>
<html lang="en">
<head>
<meta charset="utf-8">
<title>Lanternfield Systems – Brochure Spread</title>
<link href="https://fonts.googleapis.com/css2?family=Hind:wght@400;500;600&family=Titillium+Web:ital,wght@1,400;1,600&display=swap" rel="stylesheet">
<style>
  :root{
    --backdrop:#bcbcbc;
    --teal:#17a78e;
    --teal-light:#22b59d;
    --teal-dark:#1f7c74;
    --yellow:#f2ef8a;
    --bullet:#e3ec78;
    --pale-yellow:#f7f5d8;
    --pale-teal:#e3f2ee;
    --paper:#fbfbfa;
    --ink:#26383a;
    --sky:#3a6fd0;
    --white:#ffffff;
  }
  *{margin:0;padding:0;box-sizing:border-box}
  html,body{width:1200px;height:900px;overflow:hidden;background:var(--backdrop)}
  .spread{position:absolute;left:22px;top:50px;width:1156px;height:800px;display:flex;box-shadow:0 10px 30px rgba(0,0,0,.25)}
  .page{position:relative;width:578px;height:800px;overflow:hidden}

  /* Left page */
  .page--corporate{background:var(--teal);color:var(--white);font-family:"Hind",sans-serif}
  .page--corporate .lower-band{position:absolute;left:0;top:520px;width:100%;height:280px;background:var(--teal-light)}
  .hero{position:absolute;left:0;top:0}
  .section-title{position:absolute;font-family:"Titillium Web",sans-serif;font-style:italic;line-height:1;text-transform:uppercase}
  .section-title .kicker{display:block;font-size:17px;font-weight:400}
  .section-title .main{display:block;font-size:26px;font-weight:600;letter-spacing:.5px;margin-top:2px}
  .page--corporate .section-title{left:47px;top:318px}
  .intro{position:absolute;left:47px;top:373px;width:522px;font-size:11.6px;line-height:18px;text-align:justify}
  .principles{position:absolute;left:52px;top:560px;width:517px;list-style:none;display:flex;flex-direction:column;gap:8px}
  .principles li{position:relative;padding-left:28px;font-size:11.2px;line-height:14px}
  .principles svg{position:absolute;left:0;top:1px}

  /* Right page */
  .page--products{background:var(--paper);color:var(--ink);font-family:"Hind",sans-serif}
  .backdrop-shapes{position:absolute;left:0;top:0}
  .page--products .section-title{left:52px;top:52px;color:var(--ink)}
  .product{position:absolute;left:0;width:578px;height:110px}
  .product-name{position:absolute;right:196px;top:0;font-size:11px;font-weight:600;letter-spacing:.3px;text-transform:uppercase;white-space:nowrap}
  .product svg{position:absolute;left:0;top:-28px}
</style>
</head>
<body>
<div class="spread">

  <section class="page page--corporate">
    <div class="lower-band"></div>
    <svg class="hero" width="578" height="360" viewBox="0 0 578 360">
      <defs>
        <linearGradient id="sky" x1="0" y1="0" x2="1" y2="1">
          <stop offset="0" stop-color="#3b66d6"/>
          <stop offset=".55" stop-color="#4d7fd8"/>
          <stop offset="1" stop-color="#9fb3c8"/>
        </linearGradient>
      </defs>
      <path d="M70,140 Q200,60 400,6 L404,14 Q210,72 82,138 Z" fill="var(--yellow)"/>
      <path d="M440,330 Q520,352 560,362 L578,360 L578,352 Q510,344 440,330 Z" fill="var(--yellow)"/>
      <path role="img" aria-label="Photo of a modern passenger train on an elevated track under a blue sky" d="M82,130 Q230,40 420,0 L578,0 L578,348 Q330,320 82,130 Z" fill="url(#sky)"/>
    </svg>
    <h2 class="section-title"><span class="kicker">Corporate</span><span class="main">Overview</span></h2>
    <p class="intro">The Lanternfield Systems Training and Implementations Team has the primary focus of ensuring the success of our clients, and their use of Lanternfield Systems products to improve overall business processes. Our team is truly dedicated to focused, deliberate, and consultative services. With our customer-focused philosophy, we seek to always provide training and implementation services in such a way that encourages complete product utilization. We are always striving to learn and discover how to enhance the overall efficiency of our products. We are dedicated to making sure our customers have full operational visibility and realize true cost savings while using our product</p>
    <ul class="principles">
      <li><svg width="13" height="13" viewBox="0 0 13 13"><circle cx="6.5" cy="6.5" r="5.5" fill="none" stroke="var(--bullet)" stroke-width="1.5"/><circle cx="6.5" cy="6.5" r="2.3" fill="var(--bullet)"/></svg>Founded as a result of direct experience owning and managing a rail yard.</li>
      <li><svg width="13" height="13" viewBox="0 0 13 13"><circle cx="6.5" cy="6.5" r="5.5" fill="none" stroke="var(--bullet)" stroke-width="1.5"/><circle cx="6.5" cy="6.5" r="2.3" fill="var(--bullet)"/></svg>Software cost must be scalable to the terminal that is using it.</li>
      <li><svg width="13" height="13" viewBox="0 0 13 13"><circle cx="6.5" cy="6.5" r="5.5" fill="none" stroke="var(--bullet)" stroke-width="1.5"/><circle cx="6.5" cy="6.5" r="2.3" fill="var(--bullet)"/></svg>Open the lower end market and provide competitive pricing for the higher end market.</li>
      <li><svg width="13" height="13" viewBox="0 0 13 13"><circle cx="6.5" cy="6.5" r="5.5" fill="none" stroke="var(--bullet)" stroke-width="1.5"/><circle cx="6.5" cy="6.5" r="2.3" fill="var(--bullet)"/></svg>Prepare our client to use the software and understand its functionality. The transition to our software must be easy and seamless. The client needs to understand completely and confidently how to use the software before purchasing it.</li>
      <li><svg width="13" height="13" viewBox="0 0 13 13"><circle cx="6.5" cy="6.5" r="5.5" fill="none" stroke="var(--bullet)" stroke-width="1.5"/><circle cx="6.5" cy="6.5" r="2.3" fill="var(--bullet)"/></svg>Confirm and determine that the client understands the cost of the software upfront.</li>
      <li><svg width="13" height="13" viewBox="0 0 13 13"><circle cx="6.5" cy="6.5" r="5.5" fill="none" stroke="var(--bullet)" stroke-width="1.5"/><circle cx="6.5" cy="6.5" r="2.3" fill="var(--bullet)"/></svg>Continue to grow our client base while never loosing the commitment to providing quick, honest answers, and cost effective solutions.</li>
      <li><svg width="13" height="13" viewBox="0 0 13 13"><circle cx="6.5" cy="6.5" r="5.5" fill="none" stroke="var(--bullet)" stroke-width="1.5"/><circle cx="6.5" cy="6.5" r="2.3" fill="var(--bullet)"/></svg>Our current clients will attest to and our future clients will unquestionably receive the most user-friendly and robust software solutions available to manage their rail terminals.</li>
    </ul>
  </section>

  <section class="page page--products">
    <svg class="backdrop-shapes" width="578" height="800" viewBox="0 0 578 800">
      <path d="M40,0 Q420,20 578,150 L578,560 Q430,720 0,780 L0,260 Q220,200 40,0 Z" fill="var(--pale-yellow)"/>
      <path d="M0,210 Q300,260 500,520 Q540,640 578,700 L578,800 L0,800 Z" fill="var(--pale-teal)" opacity=".8"/>
      <path d="M0,560 Q260,600 420,800 L0,800 Z" fill="var(--pale-teal)"/>
    </svg>
    <h2 class="section-title"><span class="kicker">Products</span><span class="main">Overview</span></h2>

    <div class="product" style="top:122px">
      <svg width="578" height="140" viewBox="0 0 578 140">
        <path d="M0,45 L400,45 Q410,45 416,55 L430,90 L430,112 L0,112 Z" fill="var(--teal-dark)"/>
        <g role="img" aria-label="Railyard inventory software shown on a monitor and tablet">
          <rect x="414" y="2" width="122" height="86" rx="2" fill="#111"/><rect x="419" y="6" width="112" height="76" fill="#eef1f3"/>
          <rect x="406" y="52" width="76" height="60" rx="4" fill="#1b1b1b"/><rect x="411" y="57" width="66" height="48" fill="#cfd6d6"/>
        </g>
      </svg>
      <span class="product-name">Railyard Inventory Software</span>
    </div>

    <div class="product" style="top:248px">
      <svg width="578" height="140" viewBox="0 0 578 140">
        <path d="M0,45 L400,45 Q410,45 416,55 L430,90 L430,112 L0,112 Z" fill="var(--teal-dark)"/>
        <g role="img" aria-label="Railcar inspection software shown on a monitor and tablet">
          <rect x="414" y="2" width="122" height="86" rx="2" fill="#111"/><rect x="419" y="6" width="112" height="76" fill="#eef1f3"/>
          <rect x="406" y="52" width="76" height="60" rx="4" fill="#1b1b1b"/><rect x="411" y="57" width="66" height="48" fill="#cfd6d6"/>
        </g>
      </svg>
      <span class="product-name">Railcar Inspection Software</span>
    </div>

    <div class="product" style="top:374px">
      <svg width="578" height="140" viewBox="0 0 578 140">
        <path d="M0,45 L400,45 Q410,45 416,55 L430,90 L430,112 L0,112 Z" fill="var(--teal-dark)"/>
        <g role="img" aria-label="Transload software shown on a monitor and tablet">
          <rect x="414" y="2" width="122" height="86" rx="2" fill="#111"/><rect x="419" y="6" width="112" height="76" fill="#eef1f3"/>
          <rect x="406" y="52" width="76" height="60" rx="4" fill="#1b1b1b"/><rect x="411" y="57" width="66" height="48" fill="#cfd6d6"/>
        </g>
      </svg>
      <span class="product-name">Transload Software</span>
    </div>

    <div class="product" style="top:500px">
      <svg width="578" height="140" viewBox="0 0 578 140">
        <path d="M0,45 L400,45 Q410,45 416,55 L430,90 L430,112 L0,112 Z" fill="var(--teal-dark)"/>
        <g role="img" aria-label="Rail demurrage software shown on a monitor and tablet">
          <rect x="414" y="2" width="122" height="86" rx="2" fill="#111"/><rect x="419" y="6" width="112" height="76" fill="#eef1f3"/>
          <rect x="406" y="52" width="76" height="60" rx="4" fill="#1b1b1b"/><rect x="411" y="57" width="66" height="48" fill="#cfd6d6"/>
        </g>
      </svg>
      <span class="product-name">Raily Demurrage Software</span>
    </div>

    <div class="product" style="top:626px">
      <svg width="578" height="140" viewBox="0 0 578 140">
        <path d="M0,45 L400,45 Q410,45 416,55 L430,90 L430,112 L0,112 Z" fill="var(--teal-dark)"/>
        <g role="img" aria-label="Rail EDI messaging software shown on a monitor and tablet">
          <rect x="414" y="2" width="122" height="86" rx="2" fill="#111"/><rect x="419" y="6" width="112" height="76" fill="#eef1f3"/>
          <rect x="406" y="52" width="76" height="60" rx="4" fill="#1b1b1b"/><rect x="411" y="57" width="66" height="48" fill="#cfd6d6"/>
        </g>
      </svg>
      <span class="product-name">Rail EDI Messaging</span>
    </div>
  </section>

</div>
</body>
</html>
```